Clearstep Podiatry Care Advertisement Sandwich board

We need a Sandwich board design for our fungal nail clinic - please find attached the sandwich board dimensions.

The sandwich board itself will be displayed outside of a large health clinic and we need it to attract the attention of people walking by. We need a brochure holder included in the design which will hold our brochures which provides as clients with more information (please see attached also).

We are open to the designers creativity but we would like a similar theme portrayed on our board that is similar to our website (www.clearsteppodiatrycare.co.nz) and brochure that incorporates our logo which I have attached). The final design should communicate professionalism and be a minimalist look but modern to capture the attention of pedestrians.

Finally, we would like the website and phone number (07) 382 5164.

We look forward to seeing your work.

```html
<!DOCTYPE html>
<html lang="en">
<head>
<meta charset="utf-8">
<title>Clearstep Podiatry Care – Sandwich Board</title>
<link href="https://fonts.googleapis.com/css2?family=Montserrat:wght@500;600;700&family=Bebas+Neue&display=swap" rel="stylesheet">
<style>
  :root {
    --backdrop: #d7d7d7;
    --board: #ffffff;
    --brand-blue: #3c67b2;
    --brand-blue-deep: #2f55a0;
    --brand-blue-light: #6a8ac8;
    --ink: #444444;
    --ink-dark: #1e1e1e;
    --silver: #b9b9b9;
    --skin-light: #f5dccd;
    --skin-mid: #eabfa4;
  }
  * { box-sizing: border-box; margin: 0; padding: 0; }
  html, body {
    width: 804px; height: 1200px; overflow: hidden;
    background: var(--backdrop);
    font-family: "Montserrat", Arial, sans-serif;
  }
  .canvas { position: relative; width: 804px; height: 1200px; }

  /* Board face */
  .board {
    position: absolute; left: 96px; top: 344px; width: 614px; height: 787px;
    background: var(--board); overflow: hidden;
  }
  .board-photo {
    position: absolute; left: 180px; top: 0; width: 434px; height: 719px;
    background:
      radial-gradient(ellipse 22% 50% at 82% 40%, var(--skin-mid) 0%, rgba(234,191,164,0) 75%),
      radial-gradient(ellipse 26% 60% at 50% 66%, var(--skin-mid) 0%, rgba(234,191,164,0) 75%),
      linear-gradient(180deg, rgba(245,220,205,0.5) 0%, rgba(255,255,255,0) 100%);
  }
  .headline {
    position: absolute; left: 36px; top: 140px;
    color: var(--brand-blue); font-weight: 700;
    font-size: 68px; line-height: 68px; letter-spacing: -2.5px;
  }
  .more-info {
    position: absolute; left: 45px; top: 372px;
    color: var(--ink); font-weight: 700; font-size: 30px; letter-spacing: -0.8px;
  }
  .brand {
    position: absolute; left: 46px; top: 443px; width: 140px; text-align: center;
  }
  .brand-dot {
    width: 44px; height: 44px; border-radius: 50%;
    background: var(--brand-blue); margin: 0 auto 10px;
  }
  .brand-name {
    color: var(--ink-dark); font-weight: 600; font-size: 12px;
    letter-spacing: 1.8px; line-height: 16px; text-transform: uppercase;
  }
  .brand-phone {
    margin-top: 6px; color: var(--brand-blue); font-weight: 600;
    font-size: 12px; letter-spacing: 0.5px;
  }
  .cta-band {
    position: absolute; left: 0; bottom: 0; width: 614px; height: 68px;
    background: var(--brand-blue);
    display: flex; align-items: center; justify-content: center;
  }
  .cta-text {
    color: #fff; font-weight: 600; font-size: 15.5px; letter-spacing: 0.4px;
    text-transform: uppercase; white-space: nowrap;
  }
  .info-arrow { position: absolute; left: 0; top: 0; width: 804px; height: 1200px; }

  /* Brochure and holder */
  .brochure {
    position: absolute; left: 204px; top: 170px; width: 146px; height: 306px;
    background: #ffffff; overflow: hidden;
  }
  .brochure-panel { position: absolute; inset: 0; width: 146px; height: 306px; }
  .brochure-photo {
    position: absolute; left: 40px; top: 0; width: 106px; height: 200px;
    clip-path: polygon(10% 0, 100% 0, 100% 100%, 62% 100%, 22% 55%);
    background: linear-gradient(200deg, #ffffff 0%, var(--skin-light) 35%, var(--skin-mid) 65%, #ffffff 100%);
  }
  .brochure-brand {
    position: absolute; left: 22px; top: 30px; width: 60px; text-align: center;
    color: var(--ink-dark); font-weight: 600; font-size: 5px; letter-spacing: 0.6px;
    text-transform: uppercase; line-height: 7px;
  }
  .brochure-title {
    position: absolute; left: 8px; top: 206px;
    font-family: "Bebas Neue", Arial, sans-serif; color: #ffffff;
    font-size: 21px; line-height: 20px;
  }
  .brochure-tagline {
    position: absolute; left: 8px; top: 268px;
    color: var(--ink-dark); font-weight: 500; font-size: 4.5px; letter-spacing: 0.1px;
  }
  .brochure-url {
    position: absolute; left: 38px; top: 294px;
    background: var(--ink-dark); color: #fff; border-radius: 5px;
    font-size: 3.4px; padding: 1.5px 3px; font-weight: 500; white-space: nowrap;
  }
  .holder {
    position: absolute; left: 197px; top: 354px; width: 158px; height: 126px;
    background: rgba(240,240,240,0.35);
    border: 1px solid rgba(255,255,255,0.8);
    box-shadow: 0 3px 5px rgba(0,0,0,0.2);
    border-radius: 3px;
  }
</style>
</head>
<body>
<main class="canvas">
  <section class="board">
    <div class="board-photo" role="img" aria-label="Photo of a woman's smooth bare legs and feet on tiptoe with her hand resting on her leg"></div>
    <h1 class="headline">Love<br>Your<br>Toenails</h1>
    <p class="more-info">More info</p>
    <div class="brand">
      <div class="brand-dot"></div>
      <p class="brand-name">Clearstep<br>Podiatry Care</p>
      <p class="brand-phone">(07) 382 5164</p>
    </div>
    <div class="cta-band">
      <p class="cta-text">Ask about Clearstep Podiatry Care treatment today!</p>
    </div>
  </section>

  <aside class="brochure">
    <svg class="brochure-panel" viewBox="0 0 146 306" aria-hidden="true">
      <defs>
        <linearGradient id="panelBlue" x1="0" y1="0" x2="0" y2="1">
          <stop offset="0" stop-color="#2f55a0"/>
          <stop offset="1" stop-color="#6a8ac8"/>
        </linearGradient>
      </defs>
      <path d="M0 0 H22 C 10 40, 30 110, 52 150 C 75 190, 92 230, 98 300 L98 306 H0 Z" fill="url(#panelBlue)"/>
      <path d="M22 0 C 10 40, 30 110, 52 150" fill="none" stroke="#b9b9b9" stroke-width="2.5"/>
      <path d="M98 260 C 96 290, 115 302, 146 303" fill="none" stroke="#b9b9b9" stroke-width="2.5"/>
    </svg>
    <div class="brochure-photo" role="img" aria-label="Photo of bare legs and feet on tiptoe"></div>
    <p class="brochure-brand">Clearstep<br>Podiatry Care</p>
    <p class="brochure-title">Clearstep<br>Podiatry<br>Care</p>
    <p class="brochure-tagline">YOUR FUNGAL NAIL EXPERTS</p>
    <p class="brochure-url">www.clearsteppodiatrycare.co.nz</p>
  </aside>
  <div class="holder" aria-hidden="true"></div>

  <svg class="info-arrow" viewBox="0 0 804 1200" aria-hidden="true">
    <path d="M317 747 C 420 760, 490 700, 485 600 C 480 540, 440 500, 385 462"
          fill="none" stroke="#474747" stroke-width="3" stroke-linecap="round"/>
    <path d="M418 432 C 405 440, 385 437, 367 439 C 375 455, 385 470, 390 484"
          fill="none" stroke="#474747" stroke-width="4.5" stroke-linecap="round" stroke-linejoin="round"/>
  </svg>
</main>
</body>
</html>
```